Crimson Vantage Cleaning Solutions

Need a logo and business card design. I want to use a translucent business card. I want to abbreviate the name C.V.C.S. Commercial Cleaning, because my is Dov. I’d also like to incorporate a knight or something like that. I want the idea to tie in with the word Crimson. New ideas are welcome, i don’t want to limit anyone’s creativity.

Target Market(s)

Commercial Cleaning for businesses.

Contact Information for Business Card

Crimson
Vantage
Cleaning
Solutions

```html
<!DOCTYPE html>
<html lang="en">
<head>
<meta charset="utf-8">
<title>C.V.C.S. Commercial Cleaning — Business Card</title>
<link href="https://fonts.googleapis.com/css2?family=Lato:wght@400;700;900&display=swap" rel="stylesheet">
<style>
  :root {
    --bg: #d9d9d9;
    --card-white: #fcf8f7;
    --brand-blue: #1d6bb0;
    --brand-green: #8ab43a;
    --ink: #4a4a4a;
    --rule: #dedad8;
    --pattern-blue: #2a76b8;
  }
  * { margin: 0; padding: 0; box-sizing: border-box; }
  html, body { width: 1200px; height: 782px; overflow: hidden; }
  body {
    background: var(--bg);
    font-family: "Lato", sans-serif;
    display: flex;
    align-items: center;
    justify-content: center;
    gap: 60px;
  }
  .card {
    width: 520px;
    height: 297px;
    position: relative;
    box-shadow: 0 4px 14px rgba(0,0,0,0.18);
  }

  /* Front */
  .card-front {
    background: var(--card-white);
    display: flex;
    align-items: center;
  }
  .brand {
    width: 268px;
    display: flex;
    align-items: center;
    justify-content: center;
    gap: 12px;
  }
  .brand-mark {
    width: 16px;
    height: 16px;
    background: var(--brand-green);
    flex: none;
  }
  .brand-name {
    color: var(--brand-blue);
    font-weight: 900;
    font-size: 20px;
    line-height: 1.15;
    letter-spacing: 0.5px;
    text-transform: uppercase;
  }
  .divider {
    width: 1px;
    height: 190px;
    background: var(--rule);
  }
  .contact {
    padding-left: 30px;
    color: var(--ink);
    font-size: 13.5px;
    line-height: 1.35;
    letter-spacing: 0.4px;
    text-transform: uppercase;
  }
  .person-name {
    font-weight: 900;
    font-size: 17px;
    letter-spacing: 0.6px;
  }
  .person-name .first { color: var(--brand-blue); }
  .person-name .last { color: var(--brand-green); }
  .person-title {
    font-size: 12.5px;
    margin-bottom: 2px;
  }
  .contact-line {
    display: flex;
    align-items: center;
    gap: 7px;
  }
  .contact-line svg { width: 11px; height: 11px; flex: none; }
  .address { margin-top: 4px; }

  /* Back */
  .card-back {
    background: var(--brand-blue);
    display: flex;
    align-items: center;
    justify-content: center;
  }
  .back-pattern {
    position: absolute;
    inset: 0;
    background: linear-gradient(135deg, var(--brand-blue), var(--pattern-blue));
  }
  .back-name {
    position: relative;
    color: #ffffff;
    font-weight: 900;
    font-size: 22px;
    letter-spacing: 1px;
    margin-top: 110px;
  }
</style>
</head>
<body>

  <section class="card card-front" aria-label="Business card front">
    <div class="brand">
      <span class="brand-mark" aria-hidden="true"></span>
      <div class="brand-name">C.V.C.S.<br>Commercial Cleaning</div>
    </div>
    <div class="divider"></div>
    <div class="contact">
      <div class="person-name"><span class="first">Marcus</span> <span class="last">Hale</span></div>
      <div class="person-title">Managing Director</div>
      <div class="contact-line">
        <svg viewBox="0 0 12 12" aria-hidden="true"><path fill="var(--brand-green)" d="M2.5 1h2l1 2.5-1.3 1a6 6 0 0 0 3.3 3.3l1-1.3L11 7.5v2A1.5 1.5 0 0 1 9.5 11 8.5 8.5 0 0 1 1 2.5 1.5 1.5 0 0 1 2.5 1z"/></svg>
        055-204 318 660
      </div>
      <div class="contact-line">
        <svg viewBox="0 0 12 12" aria-hidden="true"><rect x="0.5" y="2" width="11" height="8" rx="1" fill="var(--brand-green)"/><path d="M1 2.8l5 3.6 5-3.6" stroke="#fff" stroke-width="1" fill="none"/></svg>
        hello@cvcsclean.com
      </div>
      <div class="contact-line">
        <svg viewBox="0 0 12 12" aria-hidden="true"><circle cx="6" cy="6" r="5.5" fill="var(--brand-green)"/><path d="M0.8 6h10.4M6 0.5c-2.4 3-2.4 8 0 11M6 0.5c2.4 3 2.4 8 0 11" stroke="#fff" stroke-width="0.8" fill="none"/></svg>
        www.cvcsclean.com
      </div>
      <div class="address">87, Harbor Row Suite 2<br>Westfield, 30718</div>
    </div>
  </section>

  <section class="card card-back" aria-label="Business card back">
    <div class="back-pattern" role="img" aria-label="Repeating brand pattern on blue background"></div>
    <div class="back-name">C.V.C.S.</div>
  </section>

</body>
</html>
```